Talents and colours poster for home office

The objective is to illustrate/communicate and remember 5 talents and 4 colours of the personality.

The infographic will be hanged on the wall of an home office. It need to be simple and clear. Illustrations and pictograms can be used. It can be artistic.

Here's the content:

5 talents,scaling in priority from #1 to #5
Ideation / creativity
Winning other over / charisma
Adaptability
Positivity
Empathy

In the files there is a description of what those mean.

You have to include 4 colours, scaling in priority from #1 to #4
Yellow
Green
Red
Blue

I made a sketch just for fun... and to show why I need professionnal skills :)

THX

Office

• offensive materials

```html
<!DOCTYPE html>
<html lang="en">
<head>
<meta charset="utf-8">
<title>Talents and Colours</title>
<link rel="stylesheet" href="https://fonts.googleapis.com/css2?family=Cinzel:wght@500&display=swap">
<style>
  :root {
    --yellow: #fff100;
    --green: #55bd7d;
    --red: #ee252b;
    --blue: #3758a4;
    --label: #ffffff;
    --label-shadow: rgba(0, 0, 0, 0.6);
    --placeholder-tone: #1e2a30;
  }
  html, body {
    margin: 0;
    padding: 0;
    overflow: hidden;
    background: #ffffff;
  }
  .poster {
    position: relative;
    width: 848px;
    height: 1200px;
    overflow: hidden;
    font-family: "Cinzel", "Times New Roman", serif;
  }
  .band {
    position: absolute;
    left: 0;
    width: 848px;
    height: 300px;
  }
  .band--yellow { top: 0;     background: var(--yellow); }
  .band--green  { top: 300px; background: var(--green); }
  .band--red    { top: 600px; background: var(--red); }
  .band--blue   { top: 900px; background: var(--blue); }

  .portrait-area {
    position: absolute;
    left: 0;
    top: 0;
    width: 848px;
    height: 1200px;
  }

  .talent {
    position: absolute;
    left: 0;
    width: 848px;
    margin: 0;
    text-align: center;
    color: var(--label);
    font-weight: 500;
    font-size: 34px;
    line-height: 1;
    letter-spacing: 0.02em;
    text-transform: uppercase;
    white-space: nowrap;
    text-shadow: 2px 3px 3px var(--label-shadow);
    transform: translateY(-50%);
  }
  .talent--1 { top: 153px; }
  .talent--2 { top: 377px; }
  .talent--3 { top: 601px; }
  .talent--4 { top: 826px; }
  .talent--5 { top: 1051px; }
</style>
</head>
<body>
  <main class="poster">
    <div class="band band--yellow"></div>
    <div class="band band--green"></div>
    <div class="band band--red"></div>
    <div class="band band--blue"></div>

    <svg class="portrait-area" viewBox="0 0 848 1200" role="img" aria-label="Illustration area: translucent portrait of a calm person with eyes closed, spanning the colour bands">
      <defs>
        <linearGradient id="portraitFade" x1="0" y1="0" x2="0" y2="1">
          <stop offset="0" stop-color="var(--placeholder-tone)" stop-opacity="0.28"/>
          <stop offset="0.7" stop-color="var(--placeholder-tone)" stop-opacity="0.2"/>
          <stop offset="1" stop-color="var(--placeholder-tone)" stop-opacity="0"/>
        </linearGradient>
      </defs>
      <rect x="200" y="250" width="448" height="870" fill="url(#portraitFade)"/>
    </svg>

    <h2 class="talent talent--1">Ideation / Creativity</h2>
    <h2 class="talent talent--2">Winning Other Over / Charisma</h2>
    <h2 class="talent talent--3">Adaptability</h2>
    <h2 class="talent talent--4">Positivity</h2>
    <h2 class="talent talent--5">Empathy</h2>
  </main>
</body>
</html>
```